updating a virtual bank "pop-up" branch banner

we need to make this more modern looking. remove the woman please. make it look like 2022 and not 1980.

```html
<!DOCTYPE html>
<html lang="en">
<head>
<meta charset="utf-8">
<title>Nidhivault – All in One Smart Device</title>
<link rel="stylesheet" href="https://fonts.googleapis.com/css2?family=Poppins:wght@400;800&display=swap">
<style>
  :root{
    --teal:#0b8fb1;
    --teal-dark:#0a7391;
    --mist-1:#eceef0;
    --mist-2:#cfd5d9;
    --ink:#2b2b2b;
    --white:#ffffff;
    --green:#6fcf86;
    --coral:#f07a62;
    --amber:#f5c04f;
    --orange:#f39a2a;
    --sky:#62b4e6;
    --rose:#ef8a8a;
    --lilac:#c59be0;
    --mint:#6fd0bd;
    --slate:#9aa1c9;
    --taupe:#a88b7f;
  }
  *{margin:0;padding:0;box-sizing:border-box}
  html,body{width:791px;height:1200px;overflow:hidden;background:var(--white)}
  .canvas{position:relative;width:791px;height:1200px;font-family:"Poppins",sans-serif}
  .banner{position:absolute;left:99px;top:105px;width:596px;height:993px;overflow:hidden;background:var(--teal)}
  .banner-bg{position:absolute;left:0;top:0}
  .brand{position:absolute;left:20px;top:60px;display:flex;align-items:center;gap:6px;
    font-weight:800;font-size:25px;color:var(--ink);letter-spacing:-0.3px}
  .brand-dot{width:12px;height:12px;background:var(--teal);border-radius:50%}
  .headline{position:absolute;left:221px;top:72px;width:335px;height:78px;background:var(--teal);
    color:var(--white);font-weight:800;font-size:35px;line-height:37px;padding:4px 0 0 29px;letter-spacing:0.2px}
  .service{position:absolute;width:130px;text-align:center;color:var(--ink);font-size:15.5px;line-height:21px}
  .service .badge{display:block;width:66px;height:66px;margin:0 auto 8px}
  .atm-art{position:absolute;left:47px;top:509px;width:377px;height:439px;
    background:linear-gradient(160deg,#9c9d9a 0%,#6f716f 45%,#4b4d4c 100%)}
  .atm-art::before{content:"";position:absolute;left:70px;top:20px;width:237px;height:43px;
    background:linear-gradient(90deg,#1f5fe0,#3d8bf2)}
  .atm-art::after{content:"";position:absolute;left:97px;top:208px;width:128px;height:103px;
    background:linear-gradient(180deg,#6fd8ff,#1a8fe0)}
</style>
</head>
<body>
<div class="canvas">
  <section class="banner">
    <svg class="banner-bg" width="596" height="993" viewBox="0 0 596 993" aria-hidden="true">
      <defs>
        <linearGradient id="mist" x1="0" y1="0" x2="1" y2="1">
          <stop offset="0" stop-color="var(--mist-1)"/>
          <stop offset="1" stop-color="var(--mist-2)"/>
        </linearGradient>
      </defs>
      <path d="M0 100 C40 240 100 420 163 520 L430 520 L430 727 C490 725 550 714 596 700 L596 0 L0 0 Z" fill="url(#mist)"/>
      <path d="M0 0 H214 C190 90 110 140 0 95 Z" fill="var(--white)"/>
      <path d="M478 150 L556 150 L478 190 Z" fill="var(--teal-dark)"/>
      <path d="M234 162 L556 152 L556 156 L234 167 Z" fill="var(--white)"/>
      <g stroke="var(--teal)" stroke-width="4" stroke-linecap="round">
        <path d="M199 70 L215 84"/><path d="M554 50 L564 64"/>
      </g>
      <g stroke="var(--white)" stroke-width="4" stroke-linecap="round">
        <path d="M196 86 L214 90"/><path d="M561 88 L577 91"/><path d="M229 57 L230 72"/>
      </g>
      <g stroke-width="4" stroke-linecap="round">
        <path d="M170 128 v12 M164 134 h12" stroke="var(--teal)"/>
        <path d="M202 136 v12 M196 142 h12" stroke="var(--teal)"/>
        <path d="M181 149 v10 M176 154 h10" stroke="var(--white)"/>
      </g>
    </svg>

    <div class="brand"><span class="brand-dot"></span>nidhivault</div>
    <h1 class="headline">ALL IN ONE<br>SMART DEVICE</h1>

    <div class="service" style="left:102px;top:213px">
      <svg class="badge" viewBox="0 0 66 66"><circle cx="33" cy="33" r="32" fill="#fff"/><path d="M4 28 A30 30 0 0 1 62 28" fill="none" stroke="var(--green)" stroke-width="4"/><g fill="none" stroke="#333" stroke-width="2"><path d="M18 40 v-8 l4-9 h22 l4 9 v8 z"/><path d="M21 32 h24"/><circle cx="24" cy="36" r="1.5"/><circle cx="42" cy="36" r="1.5"/><path d="M20 40 v4 h5 v-4 M41 40 v4 h5 v-4"/></g></svg>
      Vehicle<br>Loan</div>
    <div class="service" style="left:221px;top:213px">
      <svg class="badge" viewBox="0 0 66 66"><circle cx="33" cy="33" r="32" fill="#fff"/><path d="M4 28 A30 30 0 0 1 62 28" fill="none" stroke="var(--coral)" stroke-width="4"/><g fill="none" stroke="#333" stroke-width="2"><path d="M17 33 L33 19 L49 33"/><path d="M21 30 v15 h24 v-15"/><path d="M29 45 v-9 h8 v9"/><path d="M41 24 v-4 h3 v7"/></g></svg>
      Home<br>Loan</div>
    <div class="service" style="left:334px;top:213px">
      <svg class="badge" viewBox="0 0 66 66"><circle cx="33" cy="33" r="32" fill="#fff"/><path d="M4 28 A30 30 0 0 1 62 28" fill="none" stroke="var(--amber)" stroke-width="4"/><g fill="none" stroke="#333" stroke-width="2"><rect x="22" y="24" width="26" height="18" rx="2"/><path d="M30 24 v-4 h10 v4 M22 32 h26"/><ellipse cx="22" cy="42" rx="6" ry="2.5"/><path d="M16 42 v5 c0 3 12 3 12 0 v-5"/></g></svg>
      Business<br>Loan</div>
    <div class="service" style="left:439px;top:213px">
      <svg class="badge" viewBox="0 0 66 66"><circle cx="33" cy="33" r="32" fill="#fff"/><path d="M4 28 A30 30 0 0 1 62 28" fill="none" stroke="var(--orange)" stroke-width="4"/><g fill="#f6c443" stroke="#b07a10" stroke-width="1.2"><path d="M28 22 h10 l2 6 h-14 z"/><path d="M20 30 h10 l2 6 h-14 z"/><path d="M35 30 h10 l2 6 h-14 z"/><path d="M14 38 h10 l2 6 h-14 z"/><path d="M28 38 h10 l2 6 h-14 z"/><path d="M42 38 h10 l2 6 h-14 z"/></g></svg>
      Gold<br>Loan</div>

    <div class="service" style="left:102px;top:343px">
      <svg class="badge" viewBox="0 0 66 66"><circle cx="33" cy="33" r="32" fill="#fff"/><path d="M4 28 A30 30 0 0 1 62 28" fill="none" stroke="var(--sky)" stroke-width="4"/><rect x="16" y="24" width="34" height="20" rx="2" fill="#f5c04f" stroke="#333" stroke-width="1.6"/><circle cx="33" cy="34" r="6" fill="#fff" stroke="#333" stroke-width="1.4"/><path d="M30 31 h6 M30 33.5 h6 M31 31 c4 0 4 5 0 5 l4 4" fill="none" stroke="#333" stroke-width="1.2"/></svg>
      Personal<br>Loan</div>
    <div class="service" style="left:221px;top:343px">
      <svg class="badge" viewBox="0 0 66 66"><circle cx="33" cy="33" r="32" fill="#fff"/><path d="M4 28 A30 30 0 0 1 62 28" fill="none" stroke="var(--rose)" stroke-width="4"/><g fill="none" stroke="#333" stroke-width="2"><path d="M17 28 L33 19 L49 28 Z"/><path d="M19 31 h28 M22 31 v12 M29 31 v12 M37 31 v12 M44 31 v12 M17 44 h32 M15 47 h36"/></g></svg>
      Savings/Current<br>Account</div>
    <div class="service" style="left:334px;top:343px">
      <svg class="badge" viewBox="0 0 66 66"><circle cx="33" cy="33" r="32" fill="#fff"/><path d="M4 28 A30 30 0 0 1 62 28" fill="none" stroke="var(--lilac)" stroke-width="4"/><g fill="none" stroke="#333" stroke-width="2"><ellipse cx="33" cy="44" rx="11" ry="3.5"/><path d="M22 44 v-5 c0 4.5 22 4.5 22 0 v5"/><ellipse cx="33" cy="34" rx="11" ry="3.5"/><path d="M22 34 v5 M44 34 v5"/></g><circle cx="33" cy="23" r="5" fill="#f5c04f" stroke="#333" stroke-width="1.4"/></svg>
      Fixed<br>Deposit</div>
    <div class="service" style="left:439px;top:343px">
      <svg class="badge" viewBox="0 0 66 66"><circle cx="33" cy="33" r="32" fill="#fff"/><path d="M4 28 A30 30 0 0 1 62 28" fill="none" stroke="var(--mint)" stroke-width="4"/><g fill="none" stroke="#333" stroke-width="2"><rect x="15" y="22" width="28" height="18" rx="1.5"/><path d="M29 40 v4 M23 45 h12"/><rect x="40" y="29" width="10" height="17" rx="2" fill="#fff"/><path d="M44 43 h2"/></g></svg>
      Internet/Mobile<br>Banking</div>

    <div class="service" style="left:439px;top:472px">
      <svg class="badge" viewBox="0 0 66 66"><circle cx="33" cy="33" r="32" fill="#fff"/><path d="M4 28 A30 30 0 0 1 62 28" fill="none" stroke="var(--slate)" stroke-width="4"/><g fill="none" stroke="#333" stroke-width="2.2"><rect x="15" y="22" width="36" height="23" rx="3"/><rect x="20" y="27" width="7" height="5"/><path d="M20 39 h4 M27 39 h4 M34 39 h4 M41 39 h5"/></g></svg>
      Credit/Debit<br>Cards</div>
    <div class="service" style="left:439px;top:603px">
      <svg class="badge" viewBox="0 0 66 66"><circle cx="33" cy="33" r="32" fill="#fff"/><path d="M4 28 A30 30 0 0 1 62 28" fill="none" stroke="var(--taupe)" stroke-width="4"/><g fill="none" stroke="#333" stroke-width="2"><path d="M16 40 v-6 a9 9 0 0 1 18 0 v6"/><rect x="13" y="36" width="5" height="8" rx="2"/><rect x="32" y="36" width="5" height="8" rx="2"/><path d="M38 18 h14 v11 h-8 l-4 4 v-4 h-2 z"/><path d="M41 22 h8 M41 25 h6"/></g></svg>
      Customer<br>Care</div>

    <div class="atm-art" role="img" aria-label="Illustration of a wall-mounted ATM with a blue header sign, glowing screen, card slot and keypad"></div>
  </section>
</div>
</body>
</html>
```